Town Planning Consultants require lstationary design

Require a design to be used for our letterhead and report cover page. We have an approved logo.
we have attached our logo, and our temporary letterhead/cover page (SEE Cover) which we currently adapt for both purposes in the interim pending a permanent design. I have also attached an example (example report cover) of a report cover page that I like. perhaps similar with our colour scheme

Target Market(s)

?

Industry/Entity Type

Town

Colors
249fd4
3176b5

Requirements
Must have
• colours to match logo
• the text content in existing letterhead

```html
<!DOCTYPE html>
<html lang="en">
<head>
<meta charset="utf-8">
<title>Parkline Letterhead</title>
<link href="https://fonts.googleapis.com/css2?family=Lato:wght@400;700&display=swap" rel="stylesheet">
<style>
  :root {
    --page: #e8e8e8;
    --ink: #2b2b2b;
    --brand-blue: #249fd4;
    --band-blue: #2d9ad0;
    --brand-grey: #8c8c8c;
    --notch-grey: #8e8e8e;
    --rule: #c9c9c9;
    --sign-tint: #d7dcea;
  }
  * { margin: 0; padding: 0; box-sizing: border-box; }
  html, body { width: 900px; height: 1200px; overflow: hidden; }
  body {
    background: var(--page);
    font-family: "Lato", sans-serif;
    color: var(--ink);
    position: relative;
  }
  .letterhead { position: absolute; inset: 0; }
  .brand {
    position: absolute; top: 110px; left: 0; width: 100%;
    display: flex; justify-content: center; align-items: center; gap: 12px;
  }
  .brand-mark { width: 22px; height: 22px; background: var(--brand-blue); }
  .brand-name {
    font-size: 44px; font-weight: 400; color: var(--brand-blue); letter-spacing: 0.5px;
  }
  .letter-body {
    position: absolute; top: 378px; left: 65px; width: 790px;
    font-size: 14.2px; line-height: 18.6px;
  }
  .salutation { font-weight: 700; margin-bottom: 40px; }
  .letter-body p.paragraph { margin-bottom: 19px; }
  .sign-off { margin-top: 40px; position: relative; }
  .sign-off .name { font-weight: 700; }
  .signature {
    position: absolute; left: 140px; top: 18px; width: 130px; height: 46px;
    background: var(--sign-tint); border-radius: 4px;
  }
  .footer-band {
    position: absolute; left: 0; right: 0; top: 1110px; height: 66px;
    background: var(--band-blue); color: #fff; text-align: center;
    font-size: 14.5px; line-height: 22px; padding-top: 10px;
  }
  .footer-band b { font-weight: 700; }
  .footer-band .gap { display: inline-block; width: 8px; }
  .notch { position: absolute; }
  .notch-top { left: 112px; top: 1110px; }
  .notch-bottom { left: 790px; top: 1162px; }
  .page-rule {
    position: absolute; left: 0; right: 0; top: 1186px; height: 2px; background: var(--rule);
  }
</style>
</head>
<body>
<main class="letterhead">
  <header class="brand">
    <span class="brand-mark"></span>
    <span class="brand-name">Parkline</span>
  </header>

  <section class="letter-body">
    <p class="salutation">Dear Mr. Smith,</p>
    <p class="paragraph">Lorem ipsum dolor sit amet, consectetur adipiscing elit. Donec orci purus, luctus vitae dignissim eu, iaculis sed purus. Vivamus faucibus, ipsum nec aliquet viverra, leo mauris condimentum ligula, sit amet sagittis enim ligula quis arcu. Nam egestas tortor id nisi porttitor mattis. In tortor ante, ultricies in suscipit a, tempus non massa. Vivamus et auctor mi.</p>
    <p class="paragraph">Fusce vel massa nulla. Phasellus nec eros mauris, et scelerisque orci. Donec malesuada orci vitae nulla accumsan porta a id massa. Quisque accumsan iaculis magna sit amet fringilla. Maecenas consequat, magna eget tincidunt semper, odio nibh rutrum mi, id feugiat ante nisi eu risus. Vestibulum nunc orci, rhoncus a placerat in, ultricies in mi. Cras mattis varius eros, vel fringilla nisi suscipit eget.</p>
    <p class="paragraph">Quisque scelerisque sagittis nulla at porttitor. Mauris a justo et tellus interdum tristique. Sed id augue vitae urna euismod commodo aliquet a quam. Pellentesque arcu velit, cursus et malesuada ut, consequat et diam. Nullam erat sem, rhoncus id ullamcorper vitae, rhoncus et arcu. In ultricies ultricies nulla, ut rutrum nisi iaculis at. Donec eu magna a metus ornare faucibus.</p>
    <p class="paragraph">Fusce aliquet faucibus ultricies. Morbi semper, est id tincidunt gravida, sem arcu adipiscing lacus, ac bibendum nulla leo eu purus. Quisque nec diam sed risus consectetur a ccumsan quis quis nibh. Vestibulum id purus lorem.</p>

    <div class="sign-off">
      <p class="name">John Doe</p>
      <p class="role">Co-Founder &amp; CEO</p>
      <div class="signature" role="img" aria-label="Handwritten signature of John Doe"></div>
    </div>
  </section>

  <footer class="footer-band">
    <p>18 Harbour Ridge Road, CLOVERDALE NSW 2399</p>
    <p><b>P :</b> +61 (2) 5550 1234<span class="gap"></span><b>C :</b> +61 (0)400 555 012<span class="gap"></span><b>E :</b> joe@parkline.com.au<span class="gap"></span><b>W :</b> www.parkline.com.au</p>
  </footer>
  <svg class="notch notch-top" width="44" height="16" viewBox="0 0 44 16" aria-hidden="true">
    <polygon points="0,0 44,0 22,16" fill="var(--notch-grey)"/>
  </svg>
  <svg class="notch notch-bottom" width="44" height="14" viewBox="0 0 44 14" aria-hidden="true">
    <polygon points="0,14 44,14 22,0" fill="var(--notch-grey)"/>
  </svg>
  <div class="page-rule"></div>
</main>
</body>
</html>
```